Quiet Bramble Halloween 10K 2014

Our organization is a not-for-profit running group. This is a promotional print for our annual Quiet Bramble 'Dash Past the Dark' Halloween 10K on Saturday, October 18th @ 9:30. Folks can register on RACEPLOT.example. This event also hosts a Kids' 1 mile fun run.

We have great photos that can be incorporated. On the back we need to list certain basic info about the event which can be found on the postcards we have previously printed through Lumo Press. This includes pricing, location, awards/prizes, activities etc.

Target Market(s)

The audience is 20-45 males and females that enjoy running/fun

Industry/Entity Type

Event

Requirements
Must have
• Must incorporate Halloween in some way
Nice to have
• Something appealing to the eye that evokes a feeling of fun and excitement.

```html
<!DOCTYPE html>
<html lang="en">
<head>
<meta charset="utf-8">
<title>Quiet Bramble Halloween 10K 2014</title>
<link rel="stylesheet" href="https://fonts.googleapis.com/css2?family=Creepster&family=Jolly+Lodger&family=Arimo:ital,wght@0,400;0,700;1,700&family=Roboto+Condensed:ital,wght@0,400;0,700;1,700&display=swap">
<style>
  :root{
    --backdrop:#d8bb8e;
    --cream:#fdf8d6;
    --frame:#6b4088;
    --brand:#7a3e9e;
    --blood:#c8202a;
    --button:#e3252a;
    --ink:#1c1a17;
    --plum:#4e1f48;
    --fun:#4b2150;
    --music:#9c4f25;
    --blue:#2a5db0;
    --pumpkin:#f08a1c;
    --bullet:#a8431f;
  }
  *{box-sizing:border-box;margin:0;padding:0}
  html,body{width:1200px;height:500px;overflow:hidden;background:var(--backdrop)}
  .stage{position:relative;width:1200px;height:500px}
  .card{position:absolute;background:var(--cream);color:var(--ink)}
  .card > *{position:absolute}
  .card--front{left:28px;top:33px;width:557px;height:432px;border:12px solid var(--frame);font-family:"Arimo",Arial,sans-serif}
  .card--back{left:612px;top:33px;width:560px;height:430px;overflow:hidden;font-family:"Roboto Condensed","Arial Narrow",sans-serif}

  .brand-name{font-family:"Jolly Lodger",cursive;color:var(--brand);line-height:1}
  .headline{font-family:"Creepster",cursive;color:var(--blood);letter-spacing:1px;line-height:1}
  .edition{font-family:"Jolly Lodger",cursive;text-align:center;line-height:1.15;letter-spacing:.5px}
  .art{border-radius:4px}
  .art--pumpkin{background:radial-gradient(circle at 45% 55%,#f7a032,#d9670f);border-radius:50%}
  .art--pumpkin-purple{background:radial-gradient(circle at 45% 55%,#a45cc0,#6b2d86);border-radius:50%}
  .art--bunting{background:linear-gradient(90deg,var(--pumpkin),#2a2320 50%,var(--pumpkin));opacity:.85}
  .art--web{background:radial-gradient(circle,#cfcfcf,#f1ecd2 70%)}
  .art--photo{background:linear-gradient(180deg,#6f8f5a 0%,#9aa08e 35%,#8a8780 60%,#6c6a66 100%)}
  .art--bat{background:radial-gradient(ellipse at center,#111 55%,transparent 72%)}
  .art--tree{background:linear-gradient(180deg,#2b2622,#141210)}
  .art--witch{background:#141210;border-radius:50%}

  .event-time{font-family:"Jolly Lodger",cursive;font-size:25px;line-height:1.05}
  .register{left:290px;top:250px;width:192px;height:37px;background:var(--button);color:#fff;font-weight:700;font-size:18px;display:flex;align-items:center;justify-content:center;letter-spacing:.3px}
  .prices{left:232px;top:296px;list-style:none;font-size:15.5px;line-height:20px}
  .prices li{padding-left:20px;position:relative}
  .prices li::before{content:"★";color:var(--blood);position:absolute;left:0;top:0;font-size:14px}

  .location{left:53px;top:165px;color:var(--blood);font-weight:700;font-size:18px;line-height:21px;white-space:nowrap}
  .facts{left:16px;top:232px;list-style:none;font-size:12.5px;font-weight:700;line-height:18px;white-space:nowrap}
  .facts li{padding-left:13px;position:relative}
  .facts li::before{content:"";position:absolute;left:0;top:4px;width:10px;height:10px;border-radius:50%;background:var(--bullet)}
  .facts li.cont{padding-left:0}
  .facts li.cont::before{display:none}

  .activities-title{left:345px;top:16px;color:var(--blood);font-weight:700;font-size:23px;letter-spacing:.5px;font-family:"Arimo",Arial,sans-serif}
  .activities{left:282px;top:45px;font-size:12px;font-weight:700;line-height:16px;white-space:nowrap}
  .activities .indent{padding-left:40px}
  .activities .time,.activities .star{color:var(--blood)}
  .fun-list{left:300px;top:160px;width:165px;text-align:center;color:var(--fun);font-weight:700;font-size:16px;line-height:17px}
  .live{left:292px;top:262px;font-family:"Creepster",cursive;color:var(--music);font-size:27px}
  .prizes{left:300px;top:298px;font-family:"Creepster",cursive;color:var(--brand);font-size:30px}
  .awards{left:414px;top:285px;font-family:"Creepster",cursive;color:var(--ink);font-size:29px;letter-spacing:1px}
  .benefit{left:300px;top:328px;color:var(--blue);font-weight:700;font-style:italic;font-size:12.5px}
  .course{left:0;top:345px;width:560px;height:85px;background:var(--plum);color:#fff;font-size:13px;line-height:17px;text-align:center;padding:7px 20px 0}
</style>
</head>
<body>
<div class="stage">

  <section class="card card--front">
    <div class="art art--pumpkin" style="left:122px;top:14px;width:40px;height:34px" role="img" aria-label="Jack-o'-lantern illustration"></div>
    <div class="brand-name" style="left:12px;top:42px;font-size:46px">Quiet Bramble</div>
    <div class="art art--bunting" style="left:30px;top:96px;width:220px;height:26px" role="img" aria-label="Orange and black pennant bunting"></div>
    <div class="art art--web" style="left:340px;top:6px;width:72px;height:60px" role="img" aria-label="Spider web illustration"></div>
    <div class="headline" style="left:268px;top:60px;font-size:29px">DASH PAST THE DARK</div>
    <div class="edition" style="left:238px;top:98px;width:300px;font-size:23px">5th ANNUAL QUIET BRAMBLE<br>HALLOWEEN 10K 2014</div>
    <div class="art art--photo" style="left:32px;top:124px;width:188px;height:262px" role="img" aria-label="Photo of two young girls running the race holding hands"></div>
    <div class="art art--bat" style="left:226px;top:178px;width:100px;height:60px" role="img" aria-label="Bat illustration"></div>
    <div class="event-time" style="left:330px;top:158px">Saturday<br>October 18th<br>@ 9:30AM</div>
    <div class="register">REGISTER NOW</div>
    <ul class="prices">
      <li>Individual Age Group/Open - <b>$30.00</b></li>
      <li>QBR Member Registration - <b>$25.00</b></li>
      <li>Become an QBR Member and Save<br>on Registration! - <b>$50.00</b></li>
      <li>Race Day Registration - <b>$40</b></li>
    </ul>
  </section>

  <section class="card card--back">
    <div class="art art--pumpkin" style="left:22px;top:26px;width:30px;height:28px" role="img" aria-label="Jack-o'-lantern illustration"></div>
    <div class="brand-name" style="left:56px;top:10px;font-size:38px">Quiet Bramble</div>
    <div class="art art--pumpkin-purple" style="left:246px;top:30px;width:30px;height:28px" role="img" aria-label="Purple jack-o'-lantern illustration"></div>
    <div class="art art--bunting" style="left:40px;top:56px;width:222px;height:26px" role="img" aria-label="Orange and black pennant bunting"></div>
    <div class="headline" style="left:22px;top:90px;font-size:29px">DASH PAST THE DARK</div>
    <div class="edition" style="left:22px;top:121px;width:245px;font-size:17px">5th ANNUAL QUIET BRAMBLE<br>HALLOWEEN 10K 2014</div>
    <div class="location">Location: Linden School<br>12 Fernwick Street<br>Quiet Bramble</div>
    <ul class="facts">
      <li>Costumes encouraged but not required</li>
      <li>Race start/finish walking distance from train</li>
      <li class="cont">(Valley Rail River line to Millbrook Station)</li>
      <li>Kids' 1 mile Fun Run (6 &amp; Older) – $5 includes</li>
      <li class="cont">finisher medal and kids' activities</li>
      <li>Electronically timed/awards</li>
    </ul>

    <div class="activities-title">ACTIVITIES</div>
    <div class="activities">
      <span class="time">9 am</span> – Kids costume 1 mile fun run<br>
      <span class="indent">(ages 6 &amp; older) $5</span><br>
      <span class="indent">Includes finisher medals and kids' activities</span><br>
      Kids' Activities for all ages<br>
      <span class="star">★</span> $5 for non fun run participants
    </div>
    <div class="art art--tree" style="left:256px;top:165px;width:46px;height:90px" role="img" aria-label="Bare spooky tree silhouette"></div>
    <div class="art art--witch" style="left:452px;top:150px;width:84px;height:84px" role="img" aria-label="Witch on broomstick silhouette in a circle"></div>
    <div class="fun-list">Fun Bus<br>Face Painting<br>Obstacle Course<br>Halloween Crafts<br>And more</div>
    <div class="live">Live Music</div>
    <div class="prizes">PRIZES</div>
    <div class="awards">AWARDS</div>
    <div class="benefit">Race benefiting the QBR Outreach Fund</div>
    <p class="course">Enjoy a remarkable course that takes you through Historic Quiet Bramble's treasured sights including a stretch along the Greywater River with views of the Lantern Rider Bridge, Quiet Bramble Cemetery and the Old Stone Chapel. You never know what's lurking on the course in Quiet Bramble. . .</p>
  </section>

</div>
</body>
</html>
```